Marrowfield Biomedical Research Institute (MBRX) Web Design

MBRX is a non-profit organization focused on saving the lives of terminally ill patients by becoming the leaders in cutting-edge research, innovative technologies, utilizing national and international partnerships as well as the associated allopathic and naturopathic treatments necessary to do so.

Our primary focus is raising funds to support the research and acquisition of new technologies for life saving treatments which are NOT a one size fits all approach like conventional medicine but rather a marriage of the latest technologies used in combination with other new treatment possibilities for a successful end result.

Our domain is marrowfieldbrx.org

Logo files are attached.

Looking for something clean, light, healthy.

Target Market(s)

The site should look and feel towards research/scientific grant writing.
Medical professionals, Medical Scientists.

Industry/Entity Type

Medical And Science

Number of Pages Required

4 page

Requirements
Nice to have
• Here are examples of sites I like in the order of how much I like them.
• https://www.palvenhope.org/give.html
• https://www.thekqtf.org/donate-to-kqtf
• https://www.velmorecure.org/we-are-vci/join-the-cause
• https://www.tumarex.org/involved/donate.html
• https://give.dwkt.org/checkout/donation?eid=58217
• https://www.quillavent.org/how-you-can-help
• https://donate3.tumarex.org/

```html
<!DOCTYPE html>
<html lang="en">
<head>
<meta charset="utf-8">
<title>Marrowfield Biomedical Research Institute</title>
<link href="https://fonts.googleapis.com/css2?family=Ubuntu:wght@400;500;700&family=PT+Sans:wght@400;700&display=swap" rel="stylesheet">
<style>
:root{
  --blue:#1b73b9;
  --blue-dark:#0f5a96;
  --green:#5cb230;
  --ink:#222428;
  --text:#555a60;
  --muted:#9aa0a6;
  --line:#e3e3e3;
  --soft:#f4f4f4;
  --band:#ebebeb;
  --footer:#2b2d31;
  --white:#ffffff;
}
*{box-sizing:border-box;margin:0;padding:0}
html,body{width:1200px;height:3285px;overflow:hidden}
body{position:relative;background:var(--white);font-family:"PT Sans",sans-serif;color:var(--text)}
.abs{position:absolute}
h1,h2,h3,h4{font-family:"Ubuntu",sans-serif;color:var(--ink)}
.btn{position:absolute;display:flex;align-items:center;justify-content:center;gap:8px;font-family:"Ubuntu",sans-serif;font-weight:700;font-size:11px;letter-spacing:.3px;text-transform:uppercase;color:var(--white);border-radius:2px}
.btn-blue{background:var(--blue)}
.btn-green{background:var(--green)}
.btn-outline{border:2px solid var(--white)}

/* top bar */
.topbar{left:0;top:0;width:1200px;height:31px;border-bottom:1px solid var(--line)}
.topbar .social{left:199px;top:0;display:flex}
.topbar .social span{width:22px;height:30px;border-right:1px solid var(--line);display:flex;align-items:center;justify-content:center}
.topbar .social span:first-child{border-left:1px solid var(--line)}
.topbar .social span i{width:9px;height:9px;background:#b6b9bd;border-radius:2px}
.contact{top:0;height:30px;display:flex;align-items:center;gap:6px;font-size:11px;color:#7a7f85;border-left:1px solid var(--line);padding-left:12px}

/* header */
.header{left:0;top:31px;width:1200px;height:83px}
.logo{left:199px;top:14px;display:flex;align-items:center;gap:10px}
.logo .dot{width:44px;height:44px;border-radius:50%;background:var(--green)}
.logo .name{font-family:"Ubuntu",sans-serif;font-weight:700;font-size:34px;color:var(--blue);letter-spacing:1px}
.nav{left:436px;top:28px;display:flex;align-items:center;height:31px}
.nav a{font-family:"Ubuntu",sans-serif;font-weight:500;font-size:11px;text-transform:uppercase;color:var(--ink);text-decoration:none;margin-right:22px;height:31px;display:flex;align-items:center}
.nav a.active{background:var(--blue);color:var(--white);padding:0 13px;border-radius:2px}

/* hero */
.hero{left:0;top:114px;width:1200px;height:499px;background:linear-gradient(180deg,#9aa4ae 0%,#c7ccd1 45%,#7f8790 100%)}
.hero h1{right:199px;top:120px;width:700px;text-align:right;color:var(--white);font-weight:500;font-size:42px;line-height:50px}
.hero p{right:199px;top:248px;width:540px;text-align:right;color:var(--white);font-size:13px;line-height:27px}
.hero .dots{left:963px;top:411px;display:flex;gap:5px}
.hero .dots i{width:9px;height:9px;border-radius:50%;border:1px solid var(--white)}
.hero .dots i:first-child{background:var(--white)}
.arrow-tab{top:232px;width:35px;height:35px;background:var(--white);display:flex;align-items:center;justify-content:center}

/* give cards */
.give{top:618px;width:175px;height:192px;background:var(--soft);text-align:center}
.give .tab{left:65px;top:0;width:44px;height:61px;background:var(--blue);border-radius:0 0 22px 22px;display:flex;align-items:flex-end;justify-content:center;padding-bottom:10px}
.give h4{left:0;top:80px;width:175px;font-size:12px;font-weight:700;text-transform:uppercase}
.give p{left:25px;top:103px;width:125px;font-size:11px;line-height:15px}
.give .rule{left:70px;top:163px;width:35px;height:2px;background:var(--ink)}

/* about */
.about-photo{left:199px;top:887px;width:399px;height:252px;background:linear-gradient(135deg,#c8b7a6,#e8ddd2 60%,#b7a08c)}
.about-box{left:519px;top:889px;width:482px;height:283px;background:var(--white);box-shadow:0 3px 12px rgba(0,0,0,.18)}
.about-box h2{left:127px;top:50px;font-size:24px;font-weight:500;padding-left:14px;border-left:3px solid var(--green);line-height:26px}
.about-box p{left:127px;top:93px;width:330px;font-size:12px;line-height:21px;color:var(--ink)}

/* card bands */
.band{left:0;width:1200px;height:419px;background:var(--band)}
.intro-card{left:199px;top:75px;width:173px;height:284px;background:var(--white);border:1px solid #d6d6d6;box-shadow:0 2px 6px rgba(0,0,0,.12)}
.intro-card h3{left:16px;top:26px;width:150px;font-size:22px;font-weight:500;line-height:28px;border-left:3px solid var(--green);padding-left:0;border-left:none}
.intro-card .bar{left:16px;top:24px;width:30px;height:2px;background:var(--green)}
.intro-card p{left:16px;top:158px;width:140px;font-size:11px;line-height:16px;color:var(--muted)}
.feature{top:75px;width:175px}
.feature .img{left:0;top:0;width:175px;height:123px}
.feature h4{left:0;top:143px;font-size:13px;font-weight:500}
.feature p{left:0;top:168px;width:170px;font-size:11px;line-height:16px;color:var(--muted)}
.feature .more{left:0;top:237px;font-family:"Ubuntu",sans-serif;font-weight:700;font-size:10px;color:var(--green);text-transform:uppercase}
.plus{left:74px;top:48px;width:28px;height:28px;border-radius:50%;border:2px solid var(--white)}

/* monthly donor */
.donor{left:0;top:1680px;width:1200px;height:405px;background:linear-gradient(90deg,#3f4145 0%,#55585c 45%,#3a3f48 100%);text-align:center}
.donor h2{left:0;top:136px;width:1200px;color:var(--white);font-size:22px;font-weight:500}
.rule-green{height:2px;width:36px;background:var(--green)}
.donor p{left:219px;top:200px;width:771px;color:var(--white);font-size:12px;line-height:25px}

/* team */
.team-head{left:0;top:2652px;width:1200px;text-align:center;font-size:22px;font-weight:500}
.member{top:2718px;width:165px;height:217px}
.member .img{left:0;top:0;width:147px;height:200px;background:linear-gradient(180deg,#e6e6e6,#cfd3d7)}
.member .bar{left:0;top:188px;width:165px;height:29px;background:var(--blue);display:flex;align-items:center;justify-content:center;font-family:"Ubuntu",sans-serif;font-size:11px;font-weight:700;color:var(--white);text-transform:uppercase}
.member .bar::after{content:"";position:absolute;right:0;top:-12px;width:18px;height:41px;background:var(--blue-dark)}

/* footer */
.footer{left:0;top:3011px;width:1200px;height:248px;background:var(--footer);color:#d8d9db}
.footer h4{color:var(--white);font-size:12px;font-weight:700;text-transform:uppercase;top:66px}
.f-item{left:199px;display:flex;gap:14px;font-size:11px;line-height:17px;align-items:flex-start}
.f-item .ic{width:22px;height:18px;display:flex;align-items:center;justify-content:center}
.links a{position:absolute;font-size:11px;color:#d8d9db;text-decoration:none}
.subscribe{left:727px;top:101px;width:274px;height:37px;background:var(--white);border-radius:2px;display:flex;align-items:center;font-size:11px;color:#777;padding-left:14px}
.subscribe .send{position:absolute;right:0;top:0;width:48px;height:37px;background:var(--green);display:flex;align-items:center;justify-content:center}
.f-social{left:727px;top:155px;display:flex;gap:9px}
.f-social i{width:28px;height:28px;border-radius:50%;border:1.5px solid #cfd0d2}
.copy{left:0;top:3259px;width:1200px;height:26px;background:var(--footer);border-top:1px solid #45484d;font-size:10px;color:#c9cacd}
</style>
</head>
<body>

<!-- top bar -->
<div class="abs topbar">
  <div class="abs social"><span><i></i></span><span><i></i></span><span><i></i></span><span><i></i></span></div>
  <div class="abs contact" style="left:676px">
    <svg width="10" height="10" viewBox="0 0 24 24"><path fill="#9aa0a6" d="M6.6 10.8c1.4 2.8 3.8 5.1 6.6 6.6l2.2-2.2c.3-.3.7-.4 1-.2 1.1.4 2.3.6 3.6.6.6 0 1 .4 1 1V20c0 .6-.4 1-1 1C10.6 21 3 13.4 3 4c0-.6.4-1 1-1h3.5c.6 0 1 .4 1 1 0 1.3.2 2.5.6 3.6.1.3 0 .7-.2 1z"/></svg>
    Call us : +1234567891
  </div>
  <div class="abs contact" style="left:845px">
    <svg width="14" height="10" viewBox="0 0 14 10"><rect width="14" height="10" fill="var(--green)"/><path d="M1 1l6 5 6-5" stroke="#fff" fill="none"/></svg>
    Mail : info@mbrx.org
  </div>
</div>

<!-- header -->
<header class="abs header">
  <div class="abs logo"><span class="dot"></span><span class="name">MBRX</span></div>
  <nav class="abs nav">
    <a class="active">About Us</a><a>Care &amp; Treatment</a><a>Research</a><a>Training</a><a>Get Involved</a><a>Ways to Give</a>
  </nav>
</header>

<!-- hero -->
<section class="abs hero" role="img" aria-label="Volunteers in matching shirts joining hands in a circle, seen from below">
  <h1 class="abs">Welcome To Marrowfield Biomedical Research Institute</h1>
  <p class="abs">Lorem Ipsum is simply dummy text of the printing and typesetting industry. Lorem Ipsum has been the industry's standard dummy text</p>
  <div class="btn btn-outline" style="left:685px;top:337px;width:149px;height:39px">Read More
    <svg width="14" height="8" viewBox="0 0 14 8"><path d="M0 4h12M9 1l3 3-3 3" stroke="#fff" stroke-width="1.6" fill="none"/></svg></div>
  <div class="btn btn-outline" style="left:847px;top:337px;width:154px;height:39px">Donate Now
    <svg width="16" height="14" viewBox="0 0 24 22"><path fill="#fff" d="M12 21 2 11C-1 7 1 1 6 1c3 0 5 2 6 4 1-2 3-4 6-4 5 0 7 6 4 10z"/></svg></div>
  <div class="abs dots"><i></i><i></i><i></i></div>
  <div class="abs arrow-tab" style="left:0"><svg width="14" height="12" viewBox="0 0 14 12"><path d="M13 6H2M6 1 1 6l5 5" stroke="var(--green)" stroke-width="2" fill="none"/></svg></div>
  <div class="abs arrow-tab" style="right:0"><svg width="14" height="12" viewBox="0 0 14 12"><path d="M1 6h11M8 1l5 5-5 5" stroke="var(--green)" stroke-width="2" fill="none"/></svg></div>
</section>

<!-- ways of giving -->
<div class="abs give" style="left:199px">
  <div class="abs tab"><svg width="24" height="24" viewBox="0 0 24 24"><rect x="8" y="2" width="10" height="16" rx="1.5" fill="none" stroke="#fff" stroke-width="1.8"/><path d="M3 14c2 0 4 2 5 4l2 4" stroke="#fff" stroke-width="1.8" fill="none"/></svg></div>
  <h4 class="abs">Give Online</h4>
  <p class="abs">Lorem Ipsum is simply dummy text of the printing and typesetting industry.</p>
  <div class="abs rule"></div>
</div>
<div class="abs give" style="left:407px">
  <div class="abs tab"><svg width="24" height="22" viewBox="0 0 24 22"><rect x="2" y="7" width="20" height="14" fill="none" stroke="#fff" stroke-width="1.8"/><path d="M2 7l10 7 10-7M6 9V2h12v7" stroke="#fff" stroke-width="1.8" fill="none"/></svg></div>
  <h4 class="abs">Give By Mail</h4>
  <p class="abs">Lorem Ipsum is simply dummy text of the printing and typesetting industry.</p>
  <div class="abs rule"></div>
</div>
<div class="abs give" style="left:615px">
  <div class="abs tab"><svg width="22" height="22" viewBox="0 0 24 24"><path fill="#fff" d="M6.6 10.8c1.4 2.8 3.8 5.1 6.6 6.6l2.2-2.2c.3-.3.7-.4 1-.2 1.1.4 2.3.6 3.6.6.6 0 1 .4 1 1V20c0 .6-.4 1-1 1C10.6 21 3 13.4 3 4c0-.6.4-1 1-1h3.5c.6 0 1 .4 1 1 0 1.3.2 2.5.6 3.6.1.3 0 .7-.2 1z"/></svg></div>
  <h4 class="abs">Give By Phone</h4>
  <p class="abs">Lorem Ipsum is simply dummy text of the printing and typesetting industry.</p>
  <div class="abs rule"></div>
</div>
<div class="abs give" style="left:823px">
  <div class="abs tab"><svg width="24" height="22" viewBox="0 0 24 22"><path d="M12 13 7 8c-2-2 0-5 2.5-4 1 .4 2 1.5 2.5 2 .5-.5 1.5-1.6 2.5-2C17 3 19 6 17 8z" fill="none" stroke="#fff" stroke-width="1.6"/><path d="M2 12l5 6h10l5-6" stroke="#fff" stroke-width="1.8" fill="none"/></svg></div>
  <h4 class="abs">Donation FAQs</h4>
  <p class="abs">Lorem Ipsum is simply dummy text of the printing and typesetting industry.</p>
  <div class="abs rule"></div>
</div>

<!-- about -->
<div class="abs about-box">
  <h2 class="abs">About Us</h2>
  <p class="abs">Lorem Ipsum is simply dummy text of the printing and type-setting industry. Lorem Ipsum has been the industry's standard dummy text ever since the 1500s, when an unknown printer took a galley of type and scrambled it to make a type specimen book.</p>
  <div class="btn btn-blue" style="left:127px;top:225px;width:127px;height:38px">Read More
    <svg width="12" height="8" viewBox="0 0 14 8"><path d="M0 4h12M9 1l3 3-3 3" stroke="#fff" stroke-width="1.6" fill="none"/></svg></div>
  <div class="btn btn-green" style="left:267px;top:225px;width:127px;height:38px">Donate Now
    <svg width="14" height="12" viewBox="0 0 24 22"><path fill="#fff" d="M12 21 2 11C-1 7 1 1 6 1c3 0 5 2 6 4 1-2 3-4 6-4 5 0 7 6 4 10z"/></svg></div>
</div>
<div class="abs about-photo" role="img" aria-label="Elderly woman and young caregiver giving thumbs up together"></div>

<!-- many ways to give -->
<section class="abs band" style="top:1261px">
  <div class="abs intro-card">
    <div class="abs bar"></div>
    <h3 class="abs">There are many ways to give to MBRX</h3>
    <p class="abs">Lorem Ipsum is simply dummy text of the printing and typesetting......</p>
    <div class="btn btn-blue" style="left:16px;top:223px;width:107px;height:33px">Read More
      <svg width="11" height="8" viewBox="0 0 14 8"><path d="M0 4h12M9 1l3 3-3 3" stroke="#fff" stroke-width="1.6" fill="none"/></svg></div>
  </div>
  <div class="abs feature" style="left:410px">
    <div class="abs img" role="img" aria-label="Group photo tinted green for memorial gifts" style="background:linear-gradient(135deg,#6fb94a,#4f9b2c)"><div class="abs plus"></div></div>
    <h4 class="abs">Memorials &amp; Dedications</h4>
    <p class="abs">Lorem Ipsum is simply dummy text of the printing and typeset-ting industry.</p>
    <span class="abs more">Read More</span>
  </div>
  <div class="abs feature" style="left:615px">
    <div class="abs img" role="img" aria-label="Older couple talking with a planner at a table" style="background:linear-gradient(135deg,#8a7a6c,#c9b9a6 60%,#6e6a70)"></div>
    <h4 class="abs">Legacy and planned giving</h4>
    <p class="abs">Lorem Ipsum is simply dummy text of the printing and typeset-ting industry.</p>
    <span class="abs more">Read More</span>
  </div>
  <div class="abs feature" style="left:823px">
    <div class="abs img" role="img" aria-label="Coworkers volunteering at a donation table" style="background:linear-gradient(135deg,#7c6d86,#c8c0c6 55%,#8a5a5a)"></div>
    <h4 class="abs">Give at work</h4>
    <p class="abs">Lorem Ipsum is simply dummy text of the printing and typeset-ting industry.</p>
    <span class="abs more">Read More</span>
  </div>
</section>

<!-- monthly donor -->
<section class="abs donor" role="img" aria-label="Smiling older woman, softly blurred behind a dark overlay">
  <svg class="abs" style="left:573px;top:72px" width="54" height="54" viewBox="0 0 24 24"><path d="M12 12 8.5 8.5C7 7 8.3 4.5 10.2 5.2c.7.3 1.4 1 1.8 1.4.4-.4 1.1-1.1 1.8-1.4 1.9-.7 3.2 1.8 1.7 3.3z" fill="#fff"/><path d="M3 11l4 5v5M21 11l-4 5v5M7 16h3M17 16h-3" stroke="#fff" stroke-width="1.8" fill="none"/></svg>
  <h2 class="abs">Become a monthly donor</h2>
  <div class="abs rule-green" style="left:582px;top:172px"></div>
  <p class="abs">Lorem Ipsum is simply dummy text of the printing and typesetting industry. Lorem Ipsum has been the industry's standard dummy text ever since the 1500s, when an unknown printer took a galley of type and scrambled it to make a type specimen book. It has survived not only five centuries, but also the leap intoelectronic typesetting, remaining essentially unchanged..</p>
  <div class="btn btn-blue" style="left:499px;top:304px;width:202px;height:37px">Become a Monthly Donor</div>
</section>

<!-- also interested -->
<section class="abs band" style="top:2085px">
  <div class="abs intro-card">
    <div class="abs bar"></div>
    <h3 class="abs">You may also be interested in</h3>
    <p class="abs">Lorem Ipsum is simply dummy text of the printing and typesetting......</p>
    <div class="btn btn-blue" style="left:16px;top:223px;width:107px;height:33px">Read More
      <svg width="11" height="8" viewBox="0 0 14 8"><path d="M0 4h12M9 1l3 3-3 3" stroke="#fff" stroke-width="1.6" fill="none"/></svg></div>
  </div>
  <div class="abs feature" style="left:410px">
    <div class="abs img" role="img" aria-label="Research team photo tinted green" style="background:linear-gradient(135deg,#6fb94a,#4f9b2c)"><div class="abs plus"></div></div>
    <h4 class="abs">Why Support MBRX?</h4>
    <p class="abs">Lorem Ipsum is simply dummy text of the printing and typeset-ting industry.</p>
    <span class="abs more">Read More</span>
  </div>
  <div class="abs feature" style="left:615px">
    <div class="abs img" role="img" aria-label="Patient with a caregiver in a bright room" style="background:linear-gradient(135deg,#b9a79a,#e2d8cf 55%,#9c8a80)"></div>
    <h4 class="abs">Meet Our Patients</h4>
    <p class="abs">Lorem Ipsum is simply dummy text of the printing and typeset-ting industry.</p>
    <span class="abs more">Read More</span>
  </div>
  <div class="abs feature" style="left:823px">
    <div class="abs img" role="img" aria-label="Group of volunteers standing outdoors" style="background:linear-gradient(135deg,#8fae7e,#c9cfc4 55%,#7d8a96)"></div>
    <h4 class="abs">Get Involved With MBRX</h4>
    <p class="abs">Lorem Ipsum is simply dummy text of the printing and typeset-ting industry.</p>
    <span class="abs more">Read More</span>
  </div>
</section>

<!-- team -->
<svg class="abs" style="left:576px;top:2580px" width="48" height="48" viewBox="0 0 24 24"><path d="M12 12 8.5 8.5C7 7 8.3 4.5 10.2 5.2c.7.3 1.4 1 1.8 1.4.4-.4 1.1-1.1 1.8-1.4 1.9-.7 3.2 1.8 1.7 3.3z" fill="var(--blue)"/><path d="M3 11l4 5v5M21 11l-4 5v5M7 16h3M17 16h-3" stroke="var(--blue)" stroke-width="1.8" fill="none"/></svg>
<h2 class="abs team-head">Our Team</h2>
<div class="abs rule-green" style="left:582px;top:2676px"></div>

<div class="abs member" style="left:199px"><div class="abs img" role="img" aria-label="Portrait of a team member"></div><div class="abs bar">Dale Orwin</div></div>
<div class="abs member" style="left:414px"><div class="abs img" role="img" aria-label="Portrait of a team member"></div><div class="abs bar">Nessa Lund</div></div>
<div class="abs member" style="left:620px"><div class="abs img" role="img" aria-label="Portrait of a team member"></div><div class="abs bar">Mira Holt</div></div>
<div class="abs member" style="left:834px"><div class="abs img" role="img" aria-label="Portrait of a team member"></div><div class="abs bar">Dale Orwin</div></div>

<!-- footer -->
<footer class="abs footer">
  <h4 class="abs" style="left:199px">Keep in Touch</h4>
  <div class="abs f-item" style="top:105px"><span class="ic" style="background:#fff;border-radius:2px"><svg width="12" height="12" viewBox="0 0 24 24"><path fill="var(--footer)" d="M6.6 10.8c1.4 2.8 3.8 5.1 6.6 6.6l2.2-2.2c.3-.3.7-.4 1-.2 1.1.4 2.3.6 3.6.6.6 0 1 .4 1 1V20c0 .6-.4 1-1 1C10.6 21 3 13.4 3 4c0-.6.4-1 1-1h3.5c.6 0 1 .4 1 1 0 1.3.2 2.5.6 3.6.1.3 0 .7-.2 1z"/></svg></span><span>+1234567891</span></div>
  <div class="abs f-item" style="top:145px"><span class="ic"><svg width="14" height="18" viewBox="0 0 14 18"><path d="M7 17S1 10 1 6.5a6 6 0 0 1 12 0C13 10 7 17 7 17z" fill="var(--blue)"/><circle cx="7" cy="6.5" r="2.2" fill="#fff"/></svg></span><span>Lorem Ipsum is simply dummy<br>of the printing</span></div>
  <div class="abs f-item" style="top:192px"><span class="ic"><svg width="18" height="13" viewBox="0 0 14 10"><rect width="14" height="10" fill="var(--blue)"/><path d="M1 1l6 5 6-5" stroke="#fff" fill="none"/></svg></span><span>info@mbrx.org</span></div>

  <h4 class="abs" style="left:445px">Useful Links</h4>
  <div class="links">
    <a style="left:445px;top:106px">About Us</a><a style="left:585px;top:106px">Get Involved</a>
    <a style="left:445px;top:132px">Care &amp; Treatment</a><a style="left:585px;top:132px">Ways to Give</a>
    <a style="left:445px;top:158px">Research</a><a style="left:585px;top:158px">Our History</a>
    <a style="left:445px;top:184px">Training</a><a style="left:585px;top:184px">Stories</a>
  </div>

  <h4 class="abs" style="left:727px">Stay Connected With MBRX</h4>
  <div class="abs subscribe">Enter Your E-mail...
    <span class="send"><svg width="18" height="16" viewBox="0 0 24 22"><path d="M1 10 23 1l-5 20-6-7-4 6v-8z" fill="#fff"/></svg></span></div>
  <div class="abs f-social"><i></i><i></i><i></i><i></i></div>
</footer>
<div class="abs copy">
  <span class="abs" style="left:199px;top:6px">© Copyright 2017 MBRX. All Rights Reserved.</span>
  <span class="abs" style="right:199px;top:6px">Privacy Policy &nbsp;|&nbsp; Terms and Conditions</span>
</div>

</body>
</html>
```